Morvek Menu

Hi there,
My restaurant called "Morvek" means Spice in hebrew.
We are middle eastern restaurant that specialist in dips,salads and hot bread baked on the spot and charcoal grilled meat skewers
The restaurant is pretty casual and the atmosphere is nice and customers feels like home.
on www.morvek.com.au you can see photos of the restaurant and the food.
ill add up the menus that i would like to be design please and the logo that is on the front of the shop is been add up
thank you

Target Market(s)

The regulars of the restaurant is jewish/israelis

Industry/Entity Type

Restaurant

```html
<!DOCTYPE html>
<html lang="en">
<head>
<meta charset="utf-8">
<title>Morvek – Mains From the Charcoal Grill</title>
<link rel="stylesheet" href="https://fonts.googleapis.com/css2?family=Federant&family=Marcellus&family=Alegreya:ital,wght@0,400;0,500;1,700&display=swap">
<style>
  :root {
    --ember-top: #e2301d;
    --ember-mid: #ee7a22;
    --grill-orange: #e88a3a;
    --grill-deep: #8a4a26;
    --bar-black: #1b1a1a;
    --title-red: #b3202c;
    --heading-blue: #2c3f94;
    --ink: #1c1410;
    --rule: rgba(80, 40, 20, 0.35);
    --navy: #323a78;
    --navy-soft: #5a5f9c;
    --crimson: #b01f32;
    --gold: #f3c23a;
    --cream: #f3efe6;
  }
  * { margin: 0; padding: 0; box-sizing: border-box; }
  html, body { width: 848px; height: 1200px; overflow: hidden; background: #fff; }
  .menu {
    position: relative; width: 848px; height: 1200px; overflow: hidden;
    font-family: "Alegreya", Georgia, serif; color: var(--ink);
  }
  .menu-backdrop {
    position: absolute; inset: 0;
    background:
      radial-gradient(ellipse 60% 35% at 50% 62%, rgba(255,210,140,0.35), transparent 70%),
      linear-gradient(180deg, var(--ember-top) 0%, var(--ember-mid) 5%, #f09a4a 22%, var(--grill-orange) 40%, #b86a36 62%, var(--grill-deep) 80%, #5a3020 100%);
  }
  .brand-bar {
    position: absolute; left: 0; top: 51px; width: 848px; height: 159px;
    background: var(--bar-black);
  }
  .brand {
    position: absolute; left: 50%; top: 28px; transform: translateX(-50%);
    display: flex; flex-direction: column; align-items: center; gap: 18px;
  }
  .brand-name {
    font-family: "Marcellus", Georgia, serif; font-size: 54px; line-height: 1;
    color: var(--cream); letter-spacing: 1px;
  }
  .brand-mark { width: 14px; height: 14px; border-radius: 50%; background: var(--cream); }
  .page-title {
    position: absolute; left: 0; width: 848px; top: 232px; text-align: center;
    font-family: "Federant", Georgia, serif; font-size: 50px; color: var(--title-red);
    font-weight: 400; letter-spacing: 1.5px;
  }
  .section-heading {
    font-family: "Marcellus", Georgia, serif; color: var(--heading-blue);
    font-size: 23px; font-weight: 400; text-align: center; line-height: 34px;
  }
  .plates { position: absolute; left: 61px; top: 318px; width: 344px; }
  .plates .note {
    font-style: italic; font-weight: 700; font-size: 12.5px; text-align: center;
    line-height: 17px; margin: -2px -4px 4px;
  }
  .shashlik { position: absolute; left: 432px; top: 318px; width: 296px; }
  .shashlik .section-heading { line-height: 34px; }
  .price-list { list-style: none; }
  .price-list li {
    display: flex; justify-content: space-between; align-items: baseline;
    font-size: 15px; font-weight: 500; height: 25.6px; line-height: 25px;
    border-bottom: 1px solid var(--rule);
  }
  .shashlik .price-list { margin-top: 2px; }
  .plates .price-list { width: 344px; }
  .shashlik .price-list li { border-bottom-color: rgba(80,40,20,0.2); }
  .badge {
    position: absolute; border-radius: 50%; color: var(--cream);
    font-family: "Marcellus", Georgia, serif; text-align: center;
  }
  .badge-sides { left: 50px; top: 590px; width: 338px; height: 338px; background: var(--navy); }
  .badge-kids { left: 395px; top: 523px; width: 410px; height: 410px; background: var(--crimson); }
  .flourish { position: absolute; left: 50%; transform: translateX(-50%); border-radius: 40px; }
  .badge-sides .flourish { width: 270px; height: 46px; background: var(--navy-soft); opacity: 0.75; }
  .badge-kids .flourish { width: 330px; height: 56px; background: var(--gold); }
  .badge-heading { font-size: 22px; font-weight: 400; }
  .badge-kids .badge-heading { font-size: 25px; line-height: 36px; }
  .badge-list { list-style: none; margin: 0 auto; }
  .badge-list li {
    display: flex; justify-content: space-between; font-size: 14.5px;
    height: 25.6px; line-height: 25px; border-bottom: 1px solid rgba(255,255,255,0.25);
  }
  .set-menu-wave { position: absolute; left: 0; top: 955px; width: 848px; height: 245px; }
  .set-menu {
    position: absolute; left: 0; top: 982px; width: 848px; text-align: center;
    font-family: "Marcellus", Georgia, serif; color: var(--cream);
  }
  .set-menu h2 { font-weight: 400; font-size: 24px; color: var(--gold); line-height: 36px; }
  .set-menu ul { list-style: none; width: 412px; margin: 0 auto; }
  .set-menu li {
    font-size: 14.5px; line-height: 25.6px; border-bottom: 1px solid rgba(255,255,255,0.22);
  }
  .set-menu .minimum {
    font-family: "Alegreya", Georgia, serif; font-style: italic; font-size: 12px;
    color: var(--gold); margin-top: 4px;
  }
</style>
</head>
<body>
<main class="menu">
  <div class="menu-backdrop" role="img" aria-label="Warm orange photo of skewers cooking over a glowing charcoal grill"></div>

  <header class="brand-bar">
    <div class="brand">
      <span class="brand-name">Morvek</span>
      <span class="brand-mark"></span>
    </div>
  </header>

  <h1 class="page-title">Mains From the Charcoal Grill</h1>

  <section class="plates">
    <h2 class="section-heading">Plates</h2>
    <p class="note">All plates served with Hummus &amp; Tahini, Chips, Israeli salad and 1 Large Shashlik of your choice &nbsp;(Serves one person)</p>
    <ul class="price-list">
      <li><span>Falafel Plate</span><span>$23.00</span></li>
      <li><span>Chicken Liver</span><span>$24.00</span></li>
      <li><span>&nbsp;Chicken Schnitzel Plate</span><span>$24.00</span></li>
      <li><span>Kofta Shashlik</span><span>$24.00</span></li>
      <li><span>Chicken Shashlik</span><span>$24.00</span></li>
      <li><span>Lamb Shashlik</span><span>$26.00</span></li>
    </ul>
  </section>

  <section class="shashlik">
    <h2 class="section-heading">Individual Shashlik<br>(1 Per serve)</h2>
    <ul class="price-list">
      <li><span>Chicken Shashlik</span><span>$10</span></li>
      <li><span>Lamb Shashlik</span><span>$11.50</span></li>
      <li><span>Kebab (Kofta) Shashlik</span><span>$10.00</span></li>
      <li><span>Chicken Liver</span><span>$9.50</span></li>
      <li><span>Schnitzel</span><span>$11.00</span></li>
    </ul>
  </section>

  <section class="badge badge-sides">
    <div class="flourish" style="top:30px" role="img" aria-label="Decorative scroll ornament"></div>
    <h2 class="badge-heading" style="margin-top:80px;line-height:34px">Sides</h2>
    <ul class="badge-list" style="width:168px">
      <li><span>Israeli Salad</span><span>$10.00</span></li>
      <li><span>Chips</span><span>$8.00</span></li>
      <li><span>Laffa</span><span>$2.50</span></li>
      <li><span>&nbsp;Mix Pickles</span><span>$6.00</span></li>
    </ul>
    <div class="flourish" style="bottom:58px" role="img" aria-label="Decorative scroll ornament"></div>
  </section>

  <section class="badge badge-kids">
    <div class="flourish" style="top:45px" role="img" aria-label="Gold decorative scroll ornament"></div>
    <h2 class="badge-heading" style="margin-top:136px">Kids Meals<br>(10 and under only)</h2>
    <ul class="badge-list" style="width:340px">
      <li><span>Schnitzel plate with chips and Israeli Salad</span><span>$10.00</span></li>
      <li><span>Falafel Plate with chips and Israeli Salad</span><span>$9.00</span></li>
    </ul>
    <div class="flourish" style="bottom:68px" role="img" aria-label="Gold decorative scroll ornament"></div>
  </section>

  <svg class="set-menu-wave" viewBox="0 0 848 245" aria-hidden="true">
    <path d="M0 42 Q424 -40 848 42 L848 245 L0 245 Z" fill="#323a78"/>
  </svg>

  <section class="set-menu">
    <h2>$35 Set Menu (per person)</h2>
    <ul>
      <li>Entrée – Salads, Dips, Laffa bread &amp; Falafel</li>
      <li>Main – 1 Shashlik of per Person (Chicken, Kofta, lamb,</li>
      <li>Liver, Schnitzel), Chips &amp; Israeli salad</li>
      <li>Dessert – Chef ’s Selection</li>
    </ul>
    <p class="minimum">(Min 6 People)</p>
  </section>
</main>
</body>
</html>
```